Corvane Bookkeeping Services business cards

looking for a double sided business card design. My logo is attached. I am looking for a design similar to the attached. Keen to see what my logo in white on the blue background would look like.

```html
<!DOCTYPE html>
<html lang="en">
<head>
<meta charset="utf-8">
<title>Corvane Bookkeeping Services – Business Cards</title>
<link rel="stylesheet" href="https://fonts.googleapis.com/css2?family=Montserrat:wght@500;700;800&family=Roboto:wght@400;500&display=swap">
<style>
  :root {
    --navy: #1f3669;
    --green: #9cbb3a;
    --white: #ffffff;
    --ink: #1a1a1a;
    --backdrop: #d9d9d9;
  }
  * { box-sizing: border-box; margin: 0; padding: 0; }
  html, body { width: 1200px; height: 856px; overflow: hidden; }
  body {
    background: var(--backdrop);
    font-family: "Roboto", Arial, sans-serif;
    position: relative;
  }
  .card {
    position: absolute;
    top: 268px;
    width: 560px;
    height: 320px;
    overflow: hidden;
    box-shadow: 0 10px 28px rgba(0,0,0,0.28);
  }
  .card--front { left: 28px; background: var(--white); }
  .card--back { left: 612px; background: var(--navy); border-bottom: 8px solid var(--green); }

  .front-swoosh { position: absolute; inset: 0; width: 560px; height: 320px; }

  .brand-block { position: absolute; left: 36px; top: 34px; }
  .brand-name {
    font-family: "Montserrat", Arial, sans-serif;
    font-weight: 800;
    color: var(--green);
    font-size: 26px;
    line-height: 1.05;
    letter-spacing: 0.2px;
  }

  .corner-mark {
    position: absolute;
    right: 40px;
    top: 34px;
    display: flex;
    align-items: center;
    gap: 10px;
  }
  .corner-mark__square { width: 26px; height: 26px; background: var(--navy); }
  .corner-mark__name {
    font-family: "Montserrat", Arial, sans-serif;
    font-weight: 700;
    font-size: 15px;
    color: var(--navy);
  }

  .person { position: absolute; left: 36px; top: 128px; }
  .person__name {
    font-family: "Montserrat", Arial, sans-serif;
    font-weight: 800;
    font-size: 19px;
    color: var(--navy);
    letter-spacing: 0.5px;
  }
  .person__name .surname { color: var(--green); }
  .person__title { font-size: 13px; color: var(--ink); margin-top: 2px; }

  .contacts { position: absolute; left: 36px; top: 196px; list-style: none; }
  .contacts li {
    display: flex; align-items: center; gap: 9px;
    font-size: 13px; color: var(--ink); line-height: 22px;
  }
  .contacts svg { width: 13px; height: 13px; fill: var(--green); flex: none; }

  .address {
    position: absolute; right: 40px; top: 108px;
    text-align: right; font-size: 13px; line-height: 19px; color: var(--ink);
  }

  .back-lockup {
    position: absolute; left: 0; right: 0; top: 0; bottom: 0;
    display: flex; align-items: center; justify-content: center; gap: 16px;
  }
  .back-lockup__square { width: 46px; height: 46px; background: var(--white); }
  .back-lockup__name {
    font-family: "Montserrat", Arial, sans-serif;
    font-weight: 800;
    color: var(--white);
    font-size: 27px;
    line-height: 1.1;
  }
</style>
</head>
<body>

  <section class="card card--front" aria-label="Business card front">
    <svg class="front-swoosh" viewBox="0 0 560 320" aria-hidden="true">
      <path d="M560,150 C450,190 360,250 290,320 L560,320 Z" fill="var(--navy)"/>
      <path d="M560,140 C440,182 345,245 270,320 L282,320 C355,250 448,190 560,150 Z" fill="var(--green)"/>
    </svg>

    <div class="brand-block">
      <p class="brand-name">Corvane<br>Bookkeeping Services</p>
    </div>

    <div class="corner-mark">
      <span class="corner-mark__square"></span>
      <span class="corner-mark__name">Corvane</span>
    </div>

    <div class="person">
      <p class="person__name">DANA <span class="surname">WHITFIELD</span></p>
      <p class="person__title">Managing Director</p>
    </div>

    <ul class="contacts">
      <li>
        <svg viewBox="0 0 24 24"><path d="M6.6 10.8a15.1 15.1 0 0 0 6.6 6.6l2.2-2.2a1 1 0 0 1 1-.25 11.4 11.4 0 0 0 3.6.57 1 1 0 0 1 1 1V20a1 1 0 0 1-1 1A17 17 0 0 1 3 4a1 1 0 0 1 1-1h3.5a1 1 0 0 1 1 1c0 1.25.2 2.45.57 3.57a1 1 0 0 1-.25 1z"/></svg>
        (555)014-2290
      </li>
      <li>
        <svg viewBox="0 0 24 24"><path d="M2 5h20v14H2z M2 5l10 8 10-8" stroke="#fff" stroke-width="1.5"/></svg>
        info@corvanebooks.com
      </li>
      <li>
        <svg viewBox="0 0 24 24"><circle cx="12" cy="12" r="10"/></svg>
        www.corvanebooks.com
      </li>
    </ul>

    <p class="address">482 Linden Park Ave, Ste<br>210, Austin, TX 78701</p>
  </section>

  <section class="card card--back" aria-label="Business card back">
    <div class="back-lockup">
      <span class="back-lockup__square"></span>
      <p class="back-lockup__name">Corvane<br>Bookkeeping Services</p>
    </div>
  </section>

</body>
</html>
```